Business Card design for a company called Tully Brook Co

I need a business card design for my oil fired boiler servicing company. I have a logo design already and Im just looking that incorporated into the business card design. card details; Tully Brook Co
Oil Burner Servicing - Mid Ulster Area
Service Engineer - Owen Madler
Mobile 07700914862
email - Tully.Brook.Co@quillpost.net
www.tullybrookco.net
I carry out Servicing, Commissioning, Fault Finding, Warranty Validation
Target Market(s)
home owners with oil fired central heating
Industry/Entity Type
Business
Contact Information for Business Card
Tully Brook Co
Tell. 07700914862
Web: www.tullybrookco.net
email Tully.Brook.Co@Quillpost.Net
Servicing Fault Finding Commissioning Warranty Validation
Look and feel

```html
<!DOCTYPE html>
<html lang="en">
<head>
<meta charset="utf-8">
<title>Tully Brook Co – Business Cards</title>
<link rel="stylesheet" href="https://fonts.googleapis.com/css2?family=Roboto:wght@300;500&family=Roboto+Condensed:wght@400&display=swap">
<style>
  :root{
    --ink:#000000;
    --leaf:#8cc63f;
    --leaf-deep:#7dbf42;
    --lime:#d4e021;
    --grey:#9a9a9a;
    --white:#ffffff;
    --backdrop:#e8e4dc;
  }
  *{margin:0;padding:0;box-sizing:border-box}
  html,body{width:1200px;height:1200px;overflow:hidden;background:var(--backdrop)}
  .card{position:absolute;left:196px;width:842px;height:468px;overflow:hidden;font-family:"Roboto",sans-serif}
  .card--front{top:110px}
  .card--back{top:603px}
  .card-shapes{position:absolute;inset:0}
  .brand{position:absolute;display:flex;align-items:center;gap:14px}
  .brand-mark{width:86px;height:86px;border-radius:50%;border:8px solid var(--leaf);flex:none}
  .brand-name{font-weight:500;font-size:38px;color:var(--leaf);line-height:1;white-space:nowrap}
  .brand-tagline{font-weight:500;font-size:10.5px;letter-spacing:1.6px;color:var(--leaf);margin-top:8px;white-space:nowrap}
  .card--front .brand{left:52px;top:58px}
  .card--back .brand{left:62px;top:101px}
  .person{position:absolute;text-align:right}
  .person-name{font-weight:300;font-size:48px;line-height:1}
  .person-role{font-weight:300;font-size:23px;margin-top:6px}
  .card--front .person{right:489px;top:252px}
  .card--front .person-name{color:var(--grey)}
  .card--front .person-role{color:var(--white)}
  .card--back .person{right:418px;top:304px}
  .card--back .person-name,.card--back .person-role{color:var(--ink)}
  .contact{position:absolute;list-style:none;font-family:"Roboto Condensed",sans-serif;color:var(--ink)}
  .contact li{position:absolute;left:0;white-space:nowrap}
  .card--front .contact{left:532px;top:0;font-size:22px}
  .card--front .contact li{height:42px;line-height:42px}
  .card--back .contact{left:526px;top:0;font-size:24px}
  .card--back .contact li{height:44px;line-height:44px}
</style>
</head>
<body>

<section class="card card--front" aria-label="Business card, front">
  <svg class="card-shapes" width="842" height="468" viewBox="0 0 842 468">
    <defs>
      <linearGradient id="frontLeaf" x1="0" y1="1" x2="1" y2="0">
        <stop offset="0" stop-color="#a8d13a"/>
        <stop offset="1" stop-color="#8cc63f"/>
      </linearGradient>
    </defs>
    <rect width="842" height="468" fill="url(#frontLeaf)"/>
    <polygon points="0,0 520,0 353,468 0,468" fill="var(--ink)"/>
    <line x1="523" y1="0" x2="356" y2="468" stroke="var(--lime)" stroke-width="4"/>
    <g class="contact-bars" fill="var(--ink)">
      <polygon points="441.5,220 474,220 474,262 426.5,262"/>
      <polygon points="423.7,270 474,270 474,312 408.7,312"/>
      <polygon points="405.8,320 474,320 474,362 390.8,362"/>
      <polygon points="388,370 474,370 474,412 373,412"/>
      <rect x="478" y="220" width="44" height="42"/>
      <rect x="478" y="270" width="44" height="42"/>
      <rect x="478" y="320" width="44" height="42"/>
      <rect x="478" y="370" width="44" height="42"/>
    </g>
    <g class="contact-icons" fill="var(--leaf)" stroke="var(--leaf)">
      <path d="M500 231a6 6 0 0 1 6 6c0 5-6 11-6 11s-6-6-6-11a6 6 0 0 1 6-6z" stroke="none"/>
      <circle cx="500" cy="237" r="2.3" fill="var(--ink)" stroke="none"/>
      <path d="M496 281l4-1 2 5-2 2c1 3 2 5 4 6l2-1 4 3-1 4c-7 0-13-10-13-18z" stroke="none"/>
      <text x="500" y="349" font-family="Roboto,sans-serif" font-size="20" font-weight="500" text-anchor="middle" stroke="none">@</text>
      <g fill="none" stroke-width="1.4">
        <circle cx="500" cy="391" r="8"/>
        <ellipse cx="500" cy="391" rx="3.5" ry="8"/>
        <line x1="492" y1="391" x2="508" y2="391"/>
        <line x1="494" y1="386" x2="506" y2="386"/>
        <line x1="494" y1="396" x2="506" y2="396"/>
      </g>
    </g>
  </svg>

  <div class="brand">
    <span class="brand-mark" aria-hidden="true"></span>
    <div>
      <div class="brand-name">Tully Brook Co</div>
      <div class="brand-tagline">OIL BURNER SERVICING - MID ULSTER AREA</div>
    </div>
  </div>

  <div class="person">
    <div class="person-name">Owen Madler</div>
    <div class="person-role">Service Engineer</div>
  </div>

  <ul class="contact">
    <li style="top:220px">#00 Adress 01, Adress, City</li>
    <li style="top:270px">077 00 914 862</li>
    <li style="top:320px">tully.brook.co@quillpost.net</li>
    <li style="top:370px">www.tullybrookco.net</li>
  </ul>
</section>

<section class="card card--back" aria-label="Business card, back">
  <svg class="card-shapes" width="842" height="468" viewBox="0 0 842 468">
    <defs>
      <linearGradient id="backLime" x1="0" y1="0" x2="1" y2="0">
        <stop offset="0" stop-color="#d4e021"/>
        <stop offset="1" stop-color="#8cc63f"/>
      </linearGradient>
      <linearGradient id="backLeaf" x1="0" y1="0" x2="1" y2="1">
        <stop offset="0" stop-color="#94c83e"/>
        <stop offset="1" stop-color="#84c141"/>
      </linearGradient>
    </defs>
    <rect width="842" height="468" fill="url(#backLeaf)"/>
    <rect x="0" y="233" width="470" height="235" fill="url(#backLime)"/>
    <rect x="0" y="0" width="470" height="233" fill="var(--ink)"/>
    <g class="contact-bars" fill="var(--ink)">
      <rect x="470" y="242" width="47" height="45"/>
      <rect x="470" y="296" width="47" height="45"/>
      <rect x="470" y="349" width="47" height="46"/>
      <rect x="470" y="403" width="47" height="65"/>
    </g>
    <g class="contact-icons" fill="var(--leaf)" stroke="var(--leaf)">
      <path d="M493 256a6.5 6.5 0 0 1 6.5 6.5c0 5.5-6.5 12-6.5 12s-6.5-6.5-6.5-12a6.5 6.5 0 0 1 6.5-6.5z" stroke="none"/>
      <circle cx="493" cy="262.5" r="2.5" fill="var(--ink)" stroke="none"/>
      <path d="M489 310l4-1 2 5-2 2c1 3 2 5 4 6l2-1 4 3-1 4c-7 0-13-10-13-18z" stroke="none"/>
      <text x="493" y="382" font-family="Roboto,sans-serif" font-size="21" font-weight="500" text-anchor="middle" stroke="none">@</text>
      <g fill="none" stroke-width="1.4">
        <circle cx="493" cy="429" r="8.5"/>
        <ellipse cx="493" cy="429" rx="3.7" ry="8.5"/>
        <line x1="484.5" y1="429" x2="501.5" y2="429"/>
        <line x1="486.5" y1="424" x2="499.5" y2="424"/>
        <line x1="486.5" y1="434" x2="499.5" y2="434"/>
      </g>
    </g>
  </svg>

  <div class="brand">
    <span class="brand-mark" aria-hidden="true"></span>
    <div>
      <div class="brand-name">Tully Brook Co</div>
      <div class="brand-tagline">OIL BURNER SERVICING - MID ULSTER AREA</div>
    </div>
  </div>

  <div class="person">
    <div class="person-name">Owen Madler</div>
    <div class="person-role">Service Engineer</div>
  </div>

  <ul class="contact">
    <li style="top:244px">#00 Adress 01, Adress, City</li>
    <li style="top:298px">077 00 914 862</li>
    <li style="top:352px">tully.brook.co@quillpost.net</li>
    <li style="top:407px">www.tullybrookco.net</li>
  </ul>
</section>

</body>
</html>
```